Powerpoint template for Meadowlark Crossing

I need a powerpoint template for my business that would also work for Google slides.
I intermittently deliver training to people and I want a nice powerpoint template, that could also work in google docs to help make production easier and more seamless for me. I also sometimes product reports and analyses that are best done in powerpoint or Google slides. I need a title page, Title and content page, section heading page and any other pages that someone normally has!

Target Market(s)

Leaders and managers in medium to large companies. I provide training and coaching services to senior staff who have got 'stuck' and want help to find their way forward.

Font styles to use
Sans Serif

Requirements
Must have
• Colours and fonts to fit with logo please.
• Must include the logo and company name.
Nice to have
• a picture for the front?

```html
<!DOCTYPE html>
<html lang="en">
<head>
<meta charset="utf-8">
<title>Meadowlark Crossing – Presentation Template</title>
<link href="https://fonts.googleapis.com/css2?family=Open+Sans:ital,wght@0,400;0,600;0,700;1,400&display=swap" rel="stylesheet">
<style>
:root{
  --purple:#4b2d8f;
  --purple-dark:#3a2275;
  --teal:#1fb49a;
  --teal-light:#3cc6ad;
  --ink:#555;
  --sheet:#e3e3e3;
  --white:#fff;
  --soft:#eeeeee;
}
*{box-sizing:border-box;margin:0;padding:0}
html,body{width:1200px;height:1076px;overflow:hidden}
body{background:var(--sheet);font-family:"Open Sans",Arial,sans-serif;position:relative;color:var(--ink)}
.slide{position:absolute;width:247px;height:139px;background:var(--white);overflow:hidden;box-shadow:0 1px 3px rgba(0,0,0,.18)}
.abs{position:absolute}
.slide-title{position:absolute;left:9px;top:7px;font-size:7px;font-weight:700;color:var(--purple);letter-spacing:.1px}
.slide-title::after{content:"";position:absolute;left:0;top:10px;width:14px;height:1px;background:var(--teal)}
.footer-line{position:absolute;left:20px;right:9px;top:131px;height:.6px;background:var(--teal-light);opacity:.7}
.footer-mark{position:absolute;left:9px;top:127px;width:6px;height:6px;border-radius:50%;background:var(--purple);opacity:.55}
.tiny{font-size:3px;line-height:4px;color:#777}
.tiny-w{font-size:3.2px;line-height:4.2px;color:var(--white)}
.label{font-size:3.8px;font-weight:700;color:var(--purple)}
.photo{position:absolute}
.ph-green{background:linear-gradient(160deg,#9ccf6a,#4f8a2e 60%,#2f5a1f)}
.ph-forest{background:linear-gradient(180deg,#c7e08b,#5d8f35 55%,#2d4d1c)}
.ph-sunset{background:linear-gradient(180deg,#f5a53a,#b8561a 55%,#2a1a12)}
.ph-mountain{background:linear-gradient(180deg,#b9d6ea,#6d8d9a 50%,#5b7b3a 80%,#3a5a2a)}
.ph-sky{background:linear-gradient(180deg,#c8e2f0,#e9f2f6 60%,#d6d6d6)}
.ph-portrait{border-radius:50%;background:radial-gradient(circle at 50% 40%,#d9d9d9,#8f8f8f)}
.ico{position:absolute;border-radius:50%}
</style>
</head>
<body>

<!-- 1 Title slide -->
<section class="slide" style="left:70px;top:60px">
  <div class="photo" style="inset:0;background:linear-gradient(180deg,#5b3fa0,#4a2d8f 60%,#3d2579)" role="img" aria-label="Tree in a meadow under a purple overlay"></div>
  <div class="abs" style="left:98px;top:0;width:52px;height:47px;background:var(--white);border-radius:0 0 3px 3px;display:flex;flex-direction:column;align-items:center;justify-content:center;gap:3px">
    <span style="width:9px;height:9px;border-radius:50%;background:var(--teal)"></span>
    <span style="font-size:5px;font-weight:600;color:var(--purple);text-align:center;line-height:6px">Meadowlark<br>Crossing</span>
  </div>
  <div class="abs" style="left:0;right:0;top:96px;text-align:center;font-size:12px;font-weight:600;color:var(--white)">Meadowlark Crossing</div>
</section>

<!-- 2 Title and content -->
<section class="slide" style="left:343px;top:60px">
  <h2 class="slide-title">EDIT TITLE HERE</h2>
  <div class="abs" style="left:9px;top:31px;width:91px;height:90px;background:var(--purple);padding:10px 8px">
    <p class="tiny-w">Lorem ipsum dolor sit amet, consectetur adipiscing elit, sed do eiusmod tempor incididunt ut labore et dolore magna aliqua. Ut enim ad minim veniam, quis nostrud exercitation ullamco laboris nisi ut aliquip ex ea commodo consequat. Duis aute irure dolor in reprehenderit in voluptate velit esse cillum dolore eu fugiat nulla pariatur.</p>
  </div>
  <div class="photo ph-green" style="left:100px;top:31px;width:147px;height:90px;background:linear-gradient(120deg,#e8d9a0,#7fae3e 45%,#5a3e22 90%)" role="img" aria-label="Young seedlings growing from soil"></div>
  <div class="footer-mark"></div><div class="footer-line"></div>
</section>

<!-- 3 Team -->
<section class="slide" style="left:617px;top:60px">
  <h2 class="slide-title">EDIT TITLE HERE</h2>
  <div class="photo ph-portrait" style="left:28px;top:37px;width:34px;height:34px" role="img" aria-label="Team member portrait"></div>
  <div class="photo ph-portrait" style="left:80px;top:37px;width:34px;height:34px" role="img" aria-label="Team member portrait"></div>
  <div class="photo ph-portrait" style="left:131px;top:37px;width:34px;height:34px" role="img" aria-label="Team member portrait"></div>
  <div class="photo ph-portrait" style="left:183px;top:37px;width:34px;height:34px" role="img" aria-label="Team member portrait"></div>
  <div class="abs" style="left:20px;top:76px;width:50px;text-align:center"><div class="label">Mira Castell</div><div class="tiny">Chief Business Officer</div></div>
  <div class="abs" style="left:72px;top:76px;width:50px;text-align:center"><div class="label">Tobias Reyes</div><div class="tiny">Vice President</div></div>
  <div class="abs" style="left:123px;top:76px;width:50px;text-align:center"><div class="label">Jonah Pardo</div><div class="tiny">Chief Medical Officer</div></div>
  <div class="abs" style="left:172px;top:76px;width:56px;text-align:center"><div class="label">Felix D Marlow</div><div class="tiny">President and CEO</div></div>
  <p class="tiny abs" style="left:20px;top:94px;width:207px;text-align:center">Lorem ipsum dolor sit amet, consectetur adipiscing elit, sed do eiusmod tempor incididunt ut labore et dolore magna aliqua. Ut enim ad minim veniam, quis nostrud exercitation ullamco laboris nisi ut aliquip ex ea commodo consequat. Duis aute irure dolor in reprehenderit in voluptate velit esse cillum dolore eu fugiat nulla pariatur sint occaecat.</p>
  <div class="footer-mark"></div><div class="footer-line"></div>
</section>

<!-- 4 Three images -->
<section class="slide" style="left:888px;top:60px">
  <h2 class="slide-title">EDIT TITLE HERE</h2>
  <div class="photo ph-forest" style="left:11px;top:23px;width:72px;height:57px" role="img" aria-label="Sunlit forest"></div>
  <div class="photo ph-forest" style="left:88px;top:23px;width:72px;height:57px;background:linear-gradient(180deg,#d7e8c0,#6a9a48 55%,#3b6a2c)" role="img" aria-label="Pine forest"></div>
  <div class="photo ph-forest" style="left:165px;top:23px;width:72px;height:57px;background:linear-gradient(180deg,#b8d66a,#5b8d2a 50%,#c9c24a)" role="img" aria-label="Tree in a green field"></div>
  <div class="abs" style="left:11px;top:80px;width:72px;height:2px;background:var(--teal)"></div>
  <div class="abs" style="left:88px;top:80px;width:72px;height:2px;background:var(--teal)"></div>
  <div class="abs" style="left:165px;top:80px;width:72px;height:2px;background:var(--teal)"></div>
  <div class="abs" style="left:11px;top:92px;width:72px;text-align:center"><div class="label">Lorem ipsum dolor</div><p class="tiny">Lorem ipsum dolor sit amet, consectetur adipiscing elit. Curabitur odio ligula, ultrices eu convallis et.</p></div>
  <div class="abs" style="left:88px;top:92px;width:72px;text-align:center"><div class="label">Lorem ipsum dolor</div><p class="tiny">Lorem ipsum dolor sit amet, consectetur adipiscing elit. Curabitur odio ligula, ultrices eu convallis et.</p></div>
  <div class="abs" style="left:165px;top:92px;width:72px;text-align:center"><div class="label">Lorem ipsum dolor</div><p class="tiny">Lorem ipsum dolor sit amet, consectetur adipiscing elit. Curabitur odio ligula, ultrices eu convallis et.</p></div>
  <div class="footer-mark"></div><div class="footer-line"></div>
</section>

<!-- 5 Icon grid -->
<section class="slide" style="left:70px;top:230px">
  <h2 class="slide-title">EDIT TITLE HERE</h2>
  <div class="abs" style="left:17px;top:30px;width:215px;display:grid;grid-template-columns:repeat(5,1fr);row-gap:8px;text-align:center">
    <div><svg width="10" height="10" viewBox="0 0 10 10"><circle cx="5" cy="4" r="3.5" fill="#4b2d8f"/><rect x="4.4" y="6" width="1.2" height="4" fill="#4b2d8f"/></svg><div class="label" style="font-size:3px">LOREM IPSUM</div><p class="tiny">Lorem ipsum dolor sit amet, adipiscing elit tempor.</p></div>
    <div><svg width="10" height="10" viewBox="0 0 10 10"><circle cx="3.5" cy="5" r="3" fill="#4b2d8f"/><circle cx="6.5" cy="4" r="3.2" fill="#4b2d8f"/></svg><div class="label" style="font-size:3px">LOREM IPSUM</div><p class="tiny">Lorem ipsum dolor sit amet, adipiscing elit tempor.</p></div>
    <div><svg width="10" height="10" viewBox="0 0 10 10"><rect x="2" y="2" width="6" height="8" rx="1" fill="#4b2d8f"/></svg><div class="label" style="font-size:3px">LOREM IPSUM</div><p class="tiny">Lorem ipsum dolor sit amet, adipiscing elit tempor.</p></div>
    <div><svg width="10" height="10" viewBox="0 0 10 10"><circle cx="5" cy="5" r="3.5" fill="#4b2d8f"/></svg><div class="label" style="font-size:3px">LOREM IPSUM</div><p class="tiny">Lorem ipsum dolor sit amet, adipiscing elit tempor.</p></div>
    <div><svg width="10" height="10" viewBox="0 0 10 10"><path d="M5 1 L8 5 L5 9 L2 5Z" fill="#4b2d8f"/></svg><div class="label" style="font-size:3px">LOREM IPSUM</div><p class="tiny">Lorem ipsum dolor sit amet, adipiscing elit tempor.</p></div>
    <div><svg width="10" height="10" viewBox="0 0 10 10"><path d="M5 1 L8.5 7 H1.5Z" fill="#4b2d8f"/><rect x="4.4" y="7" width="1.2" height="3" fill="#4b2d8f"/></svg><div class="label" style="font-size:3px">LOREM IPSUM</div><p class="tiny">Lorem ipsum dolor sit amet, adipiscing elit tempor.</p></div>
    <div><svg width="10" height="10" viewBox="0 0 10 10"><circle cx="5" cy="3.5" r="2.5" fill="#4b2d8f"/><rect x="2" y="7" width="6" height="2" fill="#4b2d8f"/></svg><div class="label" style="font-size:3px">LOREM IPSUM</div><p class="tiny">Lorem ipsum dolor sit amet, adipiscing elit tempor.</p></div>
    <div><svg width="10" height="10" viewBox="0 0 10 10"><ellipse cx="5" cy="4" rx="4" ry="2.5" fill="#4b2d8f"/><rect x="4.4" y="5" width="1.2" height="5" fill="#4b2d8f"/></svg><div class="label" style="font-size:3px">LOREM IPSUM</div><p class="tiny">Lorem ipsum dolor sit amet, adipiscing elit tempor.</p></div>
    <div><svg width="10" height="10" viewBox="0 0 10 10"><ellipse cx="5" cy="5" rx="4" ry="2.2" transform="rotate(-35 5 5)" fill="#4b2d8f"/></svg><div class="label" style="font-size:3px">LOREM IPSUM</div><p class="tiny">Lorem ipsum dolor sit amet, adipiscing elit tempor.</p></div>
    <div><svg width="10" height="10" viewBox="0 0 10 10"><path d="M5 9 V4 M5 5 L2 2 M5 5 L8 2" stroke="#4b2d8f" stroke-width="1.4" fill="none"/></svg><div class="label" style="font-size:3px">LOREM IPSUM</div><p class="tiny">Lorem ipsum dolor sit amet, adipiscing elit tempor.</p></div>
  </div>
  <div class="footer-mark"></div><div class="footer-line"></div>
</section>

<!-- 6 Text and chart -->
<section class="slide" style="left:343px;top:230px">
  <h2 class="slide-title">EDIT TITLE HERE</h2>
  <p class="tiny abs" style="left:10px;top:25px;width:118px">Lorem ipsum dolor sit amet, consectetur adipiscing elit, sed do eiusmod tempor incididunt ut labore et dolore magna aliqua. Ut enim ad minim veniam, quis nostrud exercitation ullamco laboris nisi ut aliquip ex ea commodo consequat. Duis aute irure dolor in reprehenderit in voluptate velit esse cillum dolore eu fugiat nulla pariatur. Excepteur sint occaecat cupidatat non proident. Lorem ipsum dolor sit amet, consectetur adipiscing elit, sed do eiusmod tempor incididunt ut labore et dolore magna aliqua. Ut enim ad minim veniam, quis nostrud exercitation ullamco laboris nisi ut aliquip ex ea commodo consequat. Duis aute irure dolor in reprehenderit in voluptate velit esse cillum dolore eu fugiat nulla pariatur. Excepteur sint occaecat cupidatat non proident, sunt in culpa qui officia deserunt mollit anim id est laborum sed ut perspiciatis.</p>
  <svg class="abs" style="left:135px;top:40px" width="105" height="85" viewBox="0 0 105 85">
    <g stroke="#e5e5e5" stroke-width=".4"><line x1="12" y1="10" x2="100" y2="10"/><line x1="12" y1="25" x2="100" y2="25"/><line x1="12" y1="40" x2="100" y2="40"/><line x1="12" y1="55" x2="100" y2="55"/><line x1="12" y1="70" x2="100" y2="70"/></g>
    <rect x="17" y="60" width="7" height="10" fill="#4b2d8f"/>
    <rect x="31" y="47" width="7" height="23" fill="#4b2d8f"/>
    <rect x="45" y="30" width="7" height="40" fill="#4b2d8f"/>
    <rect x="59" y="20" width="7" height="50" fill="#4b2d8f"/>
    <rect x="73" y="33" width="7" height="37" fill="#4b2d8f"/>
    <rect x="87" y="50" width="7" height="20" fill="#4b2d8f"/>
    <polyline points="20,58 34,45 48,28 62,18 76,31 90,48" fill="none" stroke="#bbb" stroke-width=".5"/>
    <rect x="51" y="6" width="22" height="6" fill="#1fb49a"/>
    <text x="62" y="10.5" font-size="3.5" fill="#fff" text-anchor="middle" font-family="Open Sans,sans-serif" font-weight="700">LOREM</text>
    <g font-size="2.5" fill="#999" font-family="Open Sans,sans-serif" text-anchor="middle"><text x="20" y="75">2013</text><text x="34" y="75">2014</text><text x="48" y="75">2015</text><text x="62" y="75">2016</text><text x="76" y="75">2017</text><text x="90" y="75">2018</text><text x="56" y="82">Lorem ipsum</text></g>
  </svg>
  <div class="footer-mark"></div><div class="footer-line"></div>
</section>

<!-- 7 Section heading -->
<section class="slide" style="left:617px;top:230px">
  <div class="photo" style="inset:0;background:linear-gradient(180deg,#3fbfa5,#1fb49a 50%,#159a84)" role="img" aria-label="Mountain lake landscape under a teal overlay"></div>
  <div class="abs" style="left:0;right:0;top:77px;height:.5px;background:rgba(255,255,255,.5)"></div>
  <svg class="abs" style="left:26px;top:91px" width="22" height="18" viewBox="0 0 22 18"><rect x="7" y="1" width="8" height="4" rx="1" fill="none" stroke="#fff" stroke-width="1.6"/><rect x="1" y="4" width="20" height="13" rx="2" fill="#fff"/></svg>
  <div class="abs" style="left:56px;top:88px;font-size:10px;font-weight:600;color:var(--white)">Section Title</div>
  <p class="tiny-w abs" style="left:56px;top:103px;width:90px;font-size:2.8px;line-height:3.6px">Lorem ipsum dolor sit amet, consectetur adipiscing elit, sed do eiusmod tempor incididunt.</p>
</section>

<!-- 8 Text with side image -->
<section class="slide" style="left:888px;top:230px">
  <h2 class="slide-title">EDIT TITLE HERE</h2>
  <p class="tiny abs" style="left:10px;top:30px;width:133px;text-align:center">Lorem ipsum dolor sit amet, consectetur adipiscing elit, sed do eiusmod tempor incididunt ut labore et dolore magna aliqua. Ut enim ad minim veniam, quis nostrud exercitation ullamco laboris nisi ut aliquip ex ea commodo consequat. Duis aute irure dolor in reprehenderit in voluptate velit esse cillum dolore eu fugiat nulla pariatur. Excepteur sint occaecat cupidatat non proident, sunt in culpa qui officia deserunt mollit anim id est laborum. Sed ut perspiciatis unde omnis iste natus error sit voluptatem accusantium.</p>
  <div class="abs" style="left:12px;top:82px;width:130px;display:grid;grid-template-columns:repeat(3,1fr);text-align:center;gap:4px">
    <div><svg width="9" height="9" viewBox="0 0 10 10"><circle cx="5" cy="4" r="3.5" fill="#4b2d8f"/><rect x="4.4" y="6" width="1.2" height="4" fill="#4b2d8f"/></svg><p class="tiny">Lorem ipsum dolor sit amet, adipiscing elit tempor.</p></div>
    <div><svg width="9" height="9" viewBox="0 0 10 10"><rect x="2" y="2" width="6" height="8" rx="1" fill="#4b2d8f"/></svg><p class="tiny">Lorem ipsum dolor sit amet, adipiscing elit tempor.</p></div>
    <div><svg width="9" height="9" viewBox="0 0 10 10"><path d="M5 9 V4 M5 5 L2 2 M5 5 L8 2" stroke="#4b2d8f" stroke-width="1.4" fill="none"/></svg><p class="tiny">Lorem ipsum dolor sit amet, adipiscing elit tempor.</p></div>
  </div>
  <div class="photo ph-mountain" style="left:150px;top:0;width:97px;height:139px;background:linear-gradient(180deg,#8fc3e6,#7a8b95 40%,#4f7a3a 70%,#3e6a2c)" role="img" aria-label="Mountain peak above a green valley"></div>
  <div class="footer-mark"></div><div class="footer-line" style="right:97px"></div>
</section>

<!-- 9 Two columns -->
<section class="slide" style="left:70px;top:397px">
  <h2 class="slide-title">EDIT TITLE HERE</h2>
  <div class="abs" style="left:13px;top:31px;width:112px;height:79px;background:var(--teal);padding:8px 7px">
    <p class="tiny-w" style="font-weight:700">• Lorem ipsum dolor sit amet, consectetur adipiscing elit, sed do eiusmod tempor incididunt ut labore et dolore magna aliqua. Ut enim ad minim veniam, quis nostrud exercitation ullamco laboris nisi ut aliquip ex ea commodo consequat. Duis aute irure dolor in reprehenderit in voluptate velit esse cillum.<br>• Excepteur sint occaecat cupidatat non proident, sunt in culpa qui officia deserunt mollit anim id est laborum.</p>
  </div>
  <div class="abs" style="left:126px;top:31px;width:109px;height:79px;background:var(--purple);padding:8px 7px">
    <p class="tiny-w" style="font-weight:700">• Lorem ipsum dolor sit amet, consectetur adipiscing elit, sed do eiusmod tempor incididunt ut labore et dolore magna aliqua. Ut enim ad minim veniam, quis nostrud exercitation ullamco laboris nisi ut aliquip ex ea commodo consequat. Duis aute irure dolor in reprehenderit in voluptate velit esse cillum.<br>• Excepteur sint occaecat cupidatat non proident, sunt in culpa qui officia deserunt mollit anim id est laborum.</p>
  </div>
  <div class="footer-mark"></div><div class="footer-line"></div>
</section>

<!-- 10 Numbered list -->
<section class="slide" style="left:338px;top:397px">
  <h2 class="slide-title">EDIT TITLE HERE</h2>
  <div class="abs" style="left:14px;top:36px;width:118px;display:flex;flex-direction:column;gap:3px">
    <div style="display:flex;height:15px;background:#f2f2f2"><span style="width:14px;background:var(--purple);color:#fff;font-size:5px;font-weight:700;display:flex;align-items:center;justify-content:center">01</span><p class="tiny" style="padding:3px 4px;color:#333;font-weight:600">Lorem ipsum dolor sit amet, consectetur adipiscing elit, sed do eiusmod tempor incididunt ut labore et dolore.</p></div>
    <div style="display:flex;height:15px;background:#e6f6f2"><span style="width:14px;background:var(--teal);color:#fff;font-size:5px;font-weight:700;display:flex;align-items:center;justify-content:center">02</span><p class="tiny" style="padding:3px 4px;color:#333;font-weight:600">Lorem ipsum dolor sit amet, consectetur adipiscing elit, sed do eiusmod tempor incididunt ut labore et dolore.</p></div>
    <div style="display:flex;height:15px;background:#f2f2f2"><span style="width:14px;background:var(--purple);color:#fff;font-size:5px;font-weight:700;display:flex;align-items:center;justify-content:center">03</span><p class="tiny" style="padding:3px 4px;color:#333;font-weight:600">Lorem ipsum dolor sit amet, consectetur adipiscing elit, sed do eiusmod tempor incididunt ut labore et dolore.</p></div>
    <div style="display:flex;height:15px;background:#e6f6f2"><span style="width:14px;background:var(--teal);color:#fff;font-size:5px;font-weight:700;display:flex;align-items:center;justify-content:center">04</span><p class="tiny" style="padding:3px 4px;color:#333;font-weight:600">Lorem ipsum dolor sit amet, consectetur adipiscing elit, sed do eiusmod tempor incididunt ut labore et dolore.</p></div>
  </div>
  <div class="photo ph-sunset" style="left:136px;top:36px;width:111px;height:70px" role="img" aria-label="Palm trees at sunset"></div>
  <div class="footer-mark"></div><div class="footer-line"></div>
</section>

<!-- 11 Icon list -->
<section class="slide" style="left:617px;top:397px">
  <h2 class="slide-title">EDIT TITLE HERE</h2>
  <div class="abs" style="left:123px;top:32px;width:.6px;height:90px;background:#ccc"></div>
  <div class="abs" style="left:38px;top:34px;width:62px;text-align:right;display:flex;flex-direction:column;gap:9px">
    <div><div class="label" style="font-size:3px">Lorem ipsum dolor</div><p class="tiny">Lorem ipsum dolor sit amet, consectetur adipiscing elit sed do.</p></div>
    <div><div class="label" style="font-size:3px">Lorem ipsum dolor</div><p class="tiny">Lorem ipsum dolor sit amet, consectetur adipiscing elit sed do.</p></div>
    <div><div class="label" style="font-size:3px">Lorem ipsum dolor</div><p class="tiny">Lorem ipsum dolor sit amet, consectetur adipiscing elit sed do.</p></div>
    <div><div class="label" style="font-size:3px">Lorem ipsum dolor</div><p class="tiny">Lorem ipsum dolor sit amet, consectetur adipiscing elit sed do.</p></div>
  </div>
  <div class="ico" style="left:99px;top:35px;width:15px;height:15px;background:var(--purple)"></div>
  <div class="ico" style="left:99px;top:58px;width:15px;height:15px;background:var(--purple)"></div>
  <div class="ico" style="left:99px;top:84px;width:15px;height:15px;background:var(--purple)"></div>
  <div class="ico" style="left:99px;top:110px;width:15px;height:15px;background:var(--purple)"></div>
  <div class="ico" style="left:132px;top:35px;width:15px;height:15px;background:var(--teal)"></div>
  <div class="ico" style="left:132px;top:58px;width:15px;height:15px;background:var(--teal)"></div>
  <div class="ico" style="left:132px;top:84px;width:15px;height:15px;background:var(--teal)"></div>
  <div class="ico" style="left:132px;top:110px;width:15px;height:15px;background:var(--teal)"></div>
  <div class="abs" style="left:153px;top:34px;width:70px;display:flex;flex-direction:column;gap:9px">
    <div><div class="label" style="font-size:3px">Lorem ipsum dolor</div><p class="tiny">Lorem ipsum dolor sit amet, consectetur adipiscing elit sed do.</p></div>
    <div><div class="label" style="font-size:3px">Lorem ipsum dolor</div><p class="tiny">Lorem ipsum dolor sit amet, consectetur adipiscing elit sed do.</p></div>
    <div><div class="label" style="font-size:3px">Lorem ipsum dolor</div><p class="tiny">Lorem ipsum dolor sit amet, consectetur adipiscing elit sed do.</p></div>
    <div><div class="label" style="font-size:3px">Lorem ipsum dolor</div><p class="tiny">Lorem ipsum dolor sit amet, consectetur adipiscing elit sed do.</p></div>
  </div>
  <div class="footer-mark"></div><div class="footer-line"></div>
</section>

<!-- 12 Overlay feature -->
<section class="slide" style="left:888px;top:397px">
  <h2 class="slide-title">EDIT TITLE HERE</h2>
  <div class="abs" style="left:0;top:21px;width:140px;height:103px;background:var(--purple)"></div>
  <div class="photo ph-sky" style="left:140px;top:21px;width:107px;height:103px" role="img" aria-label="Bright terrace with sea view"></div>
  <p class="tiny-w abs" style="left:7px;top:36px;width:55px;font-weight:700;text-align:center">Lorem ipsum dolor sit amet consectetur adipiscing elit. Cras bibendum mattis leo, ac efficitur ipsum lobortis non. Praesent vitae pulvinar lorem ipsum dolor sit amet consectetur adipiscing elit.</p>
  <div class="abs" style="left:69px;top:44px;width:164px;height:50px;background:var(--white);display:grid;grid-template-columns:repeat(3,1fr);align-items:center;text-align:center">
    <div><svg width="12" height="12" viewBox="0 0 10 10"><path d="M5 9 V4 M5 5 L2 2 M5 5 L8 2" stroke="#1fb49a" stroke-width="1.4" fill="none"/></svg><div class="label" style="font-size:3.5px">LOREM</div></div>
    <div><svg width="12" height="12" viewBox="0 0 10 10"><circle cx="5" cy="4" r="3.5" fill="#1fb49a"/><rect x="4.4" y="6" width="1.2" height="4" fill="#1fb49a"/></svg><div class="label" style="font-size:3.5px">LOREM</div></div>
    <div><svg width="12" height="12" viewBox="0 0 10 10"><ellipse cx="5" cy="5" rx="4" ry="2.2" transform="rotate(-35 5 5)" fill="#1fb49a"/></svg><div class="label" style="font-size:3.5px">LOREM</div></div>
  </div>
  <div class="footer-mark"></div><div class="footer-line"></div>
</section>

<!-- 13 Puzzle -->
<section class="slide" style="left:70px;top:560px">
  <h2 class="slide-title">EDIT TITLE HERE</h2>
  <svg class="abs" style="left:75px;top:30px" width="90" height="85" viewBox="0 0 90 85" role="img" aria-label="Four interlocking puzzle pieces in teal and purple">
    <rect x="28" y="4" width="22" height="22" rx="2" transform="rotate(20 39 15)" fill="#4b2d8f"/>
    <rect x="8" y="28" width="22" height="22" rx="2" transform="rotate(20 19 39)" fill="#1fb49a"/>
    <rect x="52" y="26" width="22" height="22" rx="2" transform="rotate(20 63 37)" fill="#1fb49a"/>
    <rect x="32" y="50" width="22" height="22" rx="2" transform="rotate(20 43 61)" fill="#4b2d8f"/>
  </svg>
  <div class="abs" style="left:150px;top:32px;width:60px"><div class="label" style="font-size:3px">Lorem ipsum dolor sit</div><p class="tiny">Lorem ipsum dolor sit amet, consectetur adipiscing elit, sed</p></div>
  <div class="abs" style="left:30px;top:62px;width:55px;text-align:right"><div class="label" style="font-size:3px">Lorem ipsum dolor sit</div><p class="tiny">Lorem ipsum dolor sit amet, consectetur adipiscing elit, sed</p></div>
  <div class="abs" style="left:168px;top:70px;width:60px"><div class="label" style="font-size:3px">Lorem ipsum dolor sit</div><p class="tiny">Lorem ipsum dolor sit amet, consectetur adipiscing elit, sed</p></div>
  <div class="abs" style="left:50px;top:100px;width:55px;text-align:right"><div class="label" style="font-size:3px">Lorem ipsum dolor sit</div><p class="tiny">Lorem ipsum dolor sit amet, consectetur adipiscing elit, sed</p></div>
  <div class="footer-mark"></div><div class="footer-line"></div>
</section>

<!-- 14 Text over image -->
<section class="slide" style="left:338px;top:560px">
  <h2 class="slide-title">EDIT TITLE HERE</h2>
  <div class="abs" style="left:0;top:22px;width:78px;height:104px;background:#efefef"></div>
  <p class="tiny abs" style="left:12px;top:32px;width:62px">Lorem ipsum dolor sit amet, consectetur adipiscing elit. Donec luctus fermentum. Sed dictum, turpis ac ultricies rutrum, tellus sapien consequat erat, vitae suscipit odio justo eget sem. Vestibulum enim enim, ultricies quis placerat sed, aliquam eu ipsum. Sed a felis et diam ullamcorper convallis eu sit amet purus. Nam rhoncus risus a felis maximus aliquam. Integer quis tincidunt libero, non tincidunt ligula. Lorem ipsum dolor sit amet, consectetur adipiscing elit.</p>
  <div class="photo ph-green" style="left:78px;top:22px;width:169px;height:104px" role="img" aria-label="Sunlit park with trees"></div>
  <div class="abs" style="left:78px;top:31px;width:64px;height:87px;background:rgba(31,180,154,.92);padding:4px 5px;text-align:center"><div style="font-size:4px;font-weight:700;color:#fff;margin-bottom:3px">Lorem ipsum</div><p class="tiny-w" style="font-weight:600">Lorem ipsum dolor sit amet, consectetur adipiscing elit. Donec luctus fermentum. Sed dictum, turpis ac ultricies rutrum, tellus sapien consequat erat, vitae suscipit odio justo eget sem. Vestibulum enim enim, ultricies quis placerat sed.</p></div>
  <div class="abs" style="left:145px;top:31px;width:64px;height:87px;background:rgba(31,180,154,.92);padding:4px 5px;text-align:center"><div style="font-size:4px;font-weight:700;color:#fff;margin-bottom:3px">Lorem ipsum</div><p class="tiny-w" style="font-weight:600">Lorem ipsum dolor sit amet, consectetur adipiscing elit. Donec luctus fermentum. Sed dictum, turpis ac ultricies rutrum, tellus sapien consequat erat, vitae suscipit odio justo eget sem. Vestibulum enim enim, ultricies quis placerat sed.</p></div>
  <div class="footer-mark"></div>
</section>

<!-- 15 Two branch lists -->
<section class="slide" style="left:617px;top:560px">
  <h2 class="slide-title">EDIT TITLE HERE</h2>
  <div class="abs" style="left:29px;top:29px;width:84px;height:7px;background:var(--teal);color:#fff;font-size:3px;font-weight:700;text-align:center;line-height:7px">LOREM IPSUM</div>
  <div class="abs" style="left:132px;top:29px;width:84px;height:7px;background:var(--purple);color:#fff;font-size:3px;font-weight:700;text-align:center;line-height:7px">LOREM IPSUM</div>
  <svg class="abs" style="left:0;top:0" width="247" height="139" viewBox="0 0 247 139">
    <path d="M35 36 V112 M35 56 H48 M35 84 H48 M35 112 H48" stroke="#1fb49a" stroke-width=".8" fill="none"/>
    <circle cx="35" cy="56" r="3" fill="#1fb49a"/><circle cx="35" cy="84" r="3" fill="#1fb49a"/><circle cx="35" cy="112" r="3" fill="#1fb49a"/>
    <path d="M136 36 V112 M136 56 H150 M136 84 H150 M136 112 H150" stroke="#4b2d8f" stroke-width=".8" fill="none"/>
    <circle cx="136" cy="56" r="3" fill="#4b2d8f"/><circle cx="136" cy="84" r="3" fill="#4b2d8f"/><circle cx="136" cy="112" r="3" fill="#4b2d8f"/>
  </svg>
  <div class="abs tiny-w" style="left:48px;top:48px;width:65px;height:16px;background:var(--teal);border-radius:3px;text-align:center;padding-top:2px">Lorem ipsum dolor sit amet, consectetur adipiscing elit, sed do dolore magna aliqua.</div>
  <div class="abs tiny-w" style="left:48px;top:76px;width:65px;height:16px;background:var(--teal);border-radius:3px;text-align:center;padding-top:2px">Lorem ipsum dolor sit amet, consectetur adipiscing elit, sed do dolore magna aliqua.</div>
  <div class="abs tiny-w" style="left:48px;top:104px;width:65px;height:16px;background:var(--teal);border-radius:3px;text-align:center;padding-top:2px">Lorem ipsum dolor sit amet, consectetur adipiscing elit, sed do dolore magna aliqua.</div>
  <div class="abs tiny-w" style="left:150px;top:48px;width:66px;height:16px;background:var(--purple);border-radius:3px;text-align:center;padding-top:2px">Lorem ipsum dolor sit amet, consectetur adipiscing elit, sed do dolore magna aliqua.</div>
  <div class="abs tiny-w" style="left:150px;top:76px;width:66px;height:16px;background:var(--purple);border-radius:3px;text-align:center;padding-top:2px">Lorem ipsum dolor sit amet, consectetur adipiscing elit, sed do dolore magna aliqua.</div>
  <div class="abs tiny-w" style="left:150px;top:104px;width:66px;height:16px;background:var(--purple);border-radius:3px;text-align:center;padding-top:2px">Lorem ipsum dolor sit amet, consectetur adipiscing elit, sed do dolore magna aliqua.</div>
  <div class="footer-mark"></div><div class="footer-line"></div>
</section>

<!-- 16 Timeline -->
<section class="slide" style="left:888px;top:560px">
  <h2 class="slide-title">EDIT TITLE HERE</h2>
  <svg class="abs" style="left:0;top:0" width="247" height="139" viewBox="0 0 247 139" font-family="Open Sans,sans-serif">
    <line x1="20" y1="107" x2="228" y2="107" stroke="#1fb49a" stroke-width=".8"/>
    <g fill="#fff" stroke-width=".7">
      <circle cx="33" cy="62" r="14" stroke="#4b2d8f"/>
      <circle cx="62" cy="50" r="14" stroke="#1fb49a"/>
      <circle cx="93" cy="62" r="14" stroke="#4b2d8f"/>
      <circle cx="123" cy="50" r="14" stroke="#1fb49a"/>
      <circle cx="154" cy="62" r="14" stroke="#4b2d8f"/>
      <circle cx="185" cy="50" r="14" stroke="#1fb49a"/>
      <circle cx="215" cy="62" r="14" stroke="#4b2d8f"/>
    </g>
    <g stroke-width=".6">
      <line x1="33" y1="76" x2="33" y2="107" stroke="#4b2d8f"/><line x1="62" y1="64" x2="62" y2="107" stroke="#1fb49a"/>
      <line x1="93" y1="76" x2="93" y2="107" stroke="#4b2d8f"/><line x1="123" y1="64" x2="123" y2="107" stroke="#1fb49a"/>
      <line x1="154" y1="76" x2="154" y2="107" stroke="#4b2d8f"/><line x1="185" y1="64" x2="185" y2="107" stroke="#1fb49a"/>
      <line x1="215" y1="76" x2="215" y2="107" stroke="#4b2d8f"/>
    </g>
    <g font-size="3" font-weight="700" fill="#4b2d8f" text-anchor="middle">
      <text x="33" y="59">Edit Title</text><text x="62" y="47">Edit Title</text><text x="93" y="59">Edit Title</text><text x="123" y="47">Edit Title</text><text x="154" y="59">Edit Title</text><text x="185" y="47">Edit Title</text><text x="215" y="59">Edit Title</text>
    </g>
    <g font-size="2.4" fill="#888" text-anchor="middle">
      <text x="33" y="64">Lorem ipsum dolor</text><text x="33" y="67">sit amet elit</text>
      <text x="62" y="52">Lorem ipsum dolor</text><text x="62" y="55">sit amet elit</text>
      <text x="93" y="64">Lorem ipsum dolor</text><text x="93" y="67">sit amet elit</text>
      <text x="123" y="52">Lorem ipsum dolor</text><text x="123" y="55">sit amet elit</text>
      <text x="154" y="64">Lorem ipsum dolor</text><text x="154" y="67">sit amet elit</text>
      <text x="185" y="52">Lorem ipsum dolor</text><text x="185" y="55">sit amet elit</text>
      <text x="215" y="64">Lorem ipsum dolor</text><text x="215" y="67">sit amet elit</text>
    </g>
    <g>
      <circle cx="33" cy="87" r="5" fill="#4b2d8f"/><circle cx="62" cy="70" r="5" fill="#1fb49a"/><circle cx="93" cy="80" r="5" fill="#4b2d8f"/><circle cx="123" cy="70" r="5" fill="#1fb49a"/><circle cx="154" cy="80" r="5" fill="#4b2d8f"/><circle cx="185" cy="70" r="5" fill="#1fb49a"/><circle cx="215" cy="80" r="5" fill="#4b2d8f"/>
      <circle cx="62" cy="107" r="1.6" fill="#1fb49a"/><circle cx="123" cy="107" r="1.6" fill="#1fb49a"/><circle cx="185" cy="107" r="1.6" fill="#1fb49a"/><circle cx="93" cy="107" r="1.6" fill="#1fb49a"/><circle cx="154" cy="107" r="1.6" fill="#1fb49a"/>
    </g>
    <g font-size="3" font-weight="700" fill="#fff" text-anchor="middle">
      <text x="33" y="88">2011</text><text x="62" y="71">2012</text><text x="93" y="81">2013</text><text x="123" y="71">2014</text><text x="154" y="81">2015</text><text x="185" y="71">2016</text><text x="215" y="81">2017</text>
    </g>
  </svg>
  <div class="footer-mark"></div><div class="footer-line"></div>
</section>

<!-- 17 Six columns -->
<section class="slide" style="left:70px;top:722px">
  <h2 class="slide-title">EDIT TITLE HERE</h2>
  <div class="abs" style="left:14px;top:35px;width:218px;display:grid;grid-template-columns:repeat(6,1fr);gap:4px">
    <div><div class="ph-forest" style="height:35px" role="img" aria-label="Tropical forest"></div><div style="background:var(--purple);height:40px;padding:2px"><div style="font-size:2.8px;font-weight:700;color:#fff;text-align:center">TITLE HERE</div><p class="tiny-w" style="font-size:2.4px;line-height:3.6px">■ Lorem ipsum dolor<br>■ Lorem ipsum dolor<br>■ Lorem ipsum dolor<br>■ Lorem ipsum dolor<br>■ Lorem ipsum dolor</p></div></div>
    <div><div style="height:35px;background:linear-gradient(180deg,#9fd0ec,#8fa76a 65%,#4d6a2c)" role="img" aria-label="Savannah tree under blue sky"></div><div style="background:var(--teal);height:40px;padding:2px"><div style="font-size:2.8px;font-weight:700;color:#fff;text-align:center">TITLE HERE</div><p class="tiny-w" style="font-size:2.4px;line-height:3.6px">■ Lorem ipsum dolor<br>■ Lorem ipsum dolor<br>■ Lorem ipsum dolor<br>■ Lorem ipsum dolor<br>■ Lorem ipsum dolor</p></div></div>
    <div><div class="ph-sunset" style="height:35px" role="img" aria-label="Palm trees at sunset"></div><div style="background:var(--purple);height:40px;padding:2px"><div style="font-size:2.8px;font-weight:700;color:#fff;text-align:center">TITLE HERE</div><p class="tiny-w" style="font-size:2.4px;line-height:3.6px">■ Lorem ipsum dolor<br>■ Lorem ipsum dolor<br>■ Lorem ipsum dolor<br>■ Lorem ipsum dolor<br>■ Lorem ipsum dolor</p></div></div>
    <div><div style="height:35px;background:linear-gradient(180deg,#5aa0d8,#4f8a3a 60%,#2d5a20)" role="img" aria-label="Palm grove"></div><div style="background:var(--teal);height:40px;padding:2px"><div style="font-size:2.8px;font-weight:700;color:#fff;text-align:center">TITLE HERE</div><p class="tiny-w" style="font-size:2.4px;line-height:3.6px">■ Lorem ipsum dolor<br>■ Lorem ipsum dolor<br>■ Lorem ipsum dolor<br>■ Lorem ipsum dolor<br>■ Lorem ipsum dolor</p></div></div>
    <div><div style="height:35px;background:linear-gradient(180deg,#8fb06a,#5c7a3a 60%,#4a4030)" role="img" aria-label="Old tree roots"></div><div style="background:var(--purple);height:40px;padding:2px"><div style="font-size:2.8px;font-weight:700;color:#fff;text-align:center">TITLE HERE</div><p class="tiny-w" style="font-size:2.4px;line-height:3.6px">■ Lorem ipsum dolor<br>■ Lorem ipsum dolor<br>■ Lorem ipsum dolor<br>■ Lorem ipsum dolor<br>■ Lorem ipsum dolor</p></div></div>
    <div><div class="ph-green" style="height:35px" role="img" aria-label="Green garden"></div><div style="background:var(--teal);height:40px;padding:2px"><div style="font-size:2.8px;font-weight:700;color:#fff;text-align:center">TITLE HERE</div><p class="tiny-w" style="font-size:2.4px;line-height:3.6px">■ Lorem ipsum dolor<br>■ Lorem ipsum dolor<br>■ Lorem ipsum dolor<br>■ Lorem ipsum dolor<br>■ Lorem ipsum dolor</p></div></div>
  </div>
  <div class="footer-mark"></div><div class="footer-line"></div>
</section>

<!-- 18 Image with caption box -->
<section class="slide" style="left:338px;top:722px">
  <h2 class="slide-title">EDIT TITLE HERE</h2>
  <div class="abs" style="left:14px;top:22px;font-size:3.4px;font-weight:700;color:#333">Lorem ipsum dolor sit amet, consectetur adipiscing elit. Aenean sed tempor lorem. Suspendisse</div>
  <div class="photo ph-green" style="left:14px;top:32px;width:124px;height:55px;background:linear-gradient(180deg,#e4ecd0,#7fae4a 55%,#4e7a2a)" role="img" aria-label="Trees in a sunny park"></div>
  <div class="abs" style="left:138px;top:32px;width:95px;height:55px;background:var(--purple);padding:8px 10px">
    <div style="font-size:3.4px;font-weight:700;color:#fff;margin-bottom:2px">LOREM IPSUM</div>
    <p class="tiny-w">Lorem ipsum dolor sit amet, consectetur adipiscing elit. Aenean sed tempor lorem. Suspendisse vulputate velit ut massa commodo, quis dignissim tellus blandit. Sed imperdiet dolor sed placerat mi.</p>
  </div>
  <p class="abs" style="left:14px;top:93px;width:219px;font-size:3.5px;line-height:4.8px;color:#444">Lorem ipsum dolor sit amet, consectetur adipiscing elit. Nam porttitor lectus ac sapien rutrum, vitae commodo neque efficitur. Praesent scelerisque consectetur ante, non luctus lectus tempus id. Donec nulla leo, faucibus nec orci et, condimentum iaculis nisl. Nam pharetra tellus id tempor orci tempor sed. Proin gravida justo vitae diam tempor, non imperdiet est facilisis. Vestibulum vitae vestibulum libero, eget suscipit ligula. Quisque varius turpis sem, eget vulputate ipsum interdum vitae.</p>
  <div class="footer-mark"></div><div class="footer-line"></div>
</section>

<!-- 19 Central image with points -->
<section class="slide" style="left:617px;top:722px">
  <h2 class="slide-title">EDIT TITLE HERE</h2>
  <div class="photo" style="left:94px;top:28px;width:59px;height:96px;background:linear-gradient(180deg,#a7c7e0,#6a9a48 45%,#4f7a30 80%,#c8c8b0)" role="img" aria-label="Single tree on a hill"></div>
  <div class="abs" style="left:25px;top:30px;width:63px;text-align:right;display:flex;flex-direction:column;gap:6px">
    <div><div class="label" style="font-size:3px">Lorem ipsum dolor sit</div><p class="tiny">Lorem ipsum dolor sit amet, consectetur adipiscing elit. Cras vitae erat et augue.</p></div>
    <div><div class="label" style="font-size:3px">Lorem ipsum dolor sit</div><p class="tiny">Lorem ipsum dolor sit amet, consectetur adipiscing elit. Cras vitae erat et augue.</p></div>
    <div><div class="label" style="font-size:3px">Lorem ipsum dolor sit</div><p class="tiny">Lorem ipsum dolor sit amet, consectetur adipiscing elit. Cras vitae erat et augue.</p></div>
    <div><div class="label" style="font-size:3px">Lorem ipsum dolor sit</div><p class="tiny">Lorem ipsum dolor sit amet, consectetur adipiscing elit. Cras vitae erat et augue.</p></div>
  </div>
  <div class="abs" style="left:160px;top:30px;width:63px;display:flex;flex-direction:column;gap:6px">
    <div><div class="label" style="font-size:3px">Lorem ipsum dolor sit</div><p class="tiny">Lorem ipsum dolor sit amet, consectetur adipiscing elit. Cras vitae erat et augue.</p></div>
    <div><div class="label" style="font-size:3px">Lorem ipsum dolor sit</div><p class="tiny">Lorem ipsum dolor sit amet, consectetur adipiscing elit. Cras vitae erat et augue.</p></div>
    <div><div class="label" style="font-size:3px">Lorem ipsum dolor sit</div><p class="tiny">Lorem ipsum dolor sit amet, consectetur adipiscing elit. Cras vitae erat et augue.</p></div>
    <div><div class="label" style="font-size:3px">Lorem ipsum dolor sit</div><p class="tiny">Lorem ipsum dolor sit amet, consectetur adipiscing elit. Cras vitae erat et augue.</p></div>
  </div>
  <div class="footer-mark"></div><div class="footer-line"></div>
</section>

<!-- 20 Panorama with four points -->
<section class="slide" style="left:888px;top:722px">
  <h2 class="slide-title">EDIT TITLE HERE</h2>
  <div class="abs" style="left:14px;top:22px;font-size:3.4px;font-weight:700;color:#333">Lorem ipsum dolor sit amet, consectetur adipiscing elit. Aenean sed tempor lorem. Suspendisse</div>
  <div class="photo ph-mountain" style="left:14px;top:31px;width:218px;height:49px;background:linear-gradient(180deg,#e9eef2,#9fb3c2 35%,#3f5560 60%,#3a5a2a)" role="img" aria-label="Mountain range under clouds"></div>
  <div class="abs" style="left:14px;top:85px;width:218px;display:grid;grid-template-columns:repeat(4,1fr);gap:7px;text-align:center">
    <div><div style="background:var(--teal);height:9px;color:#fff;font-size:4px;font-weight:700;line-height:9px">A</div><p class="tiny" style="margin-top:4px">Lorem ipsum dolor sit amet, consectetur adipiscing elit. Aenean sed tempor lorem.</p></div>
    <div><div style="background:var(--purple);height:9px;color:#fff;font-size:4px;font-weight:700;line-height:9px">B</div><p class="tiny" style="margin-top:4px">Lorem ipsum dolor sit amet, consectetur adipiscing elit. Aenean sed tempor lorem.</p></div>
    <div><div style="background:var(--teal);height:9px;color:#fff;font-size:4px;font-weight:700;line-height:9px">C</div><p class="tiny" style="margin-top:4px">Lorem ipsum dolor sit amet, consectetur adipiscing elit. Aenean sed tempor lorem.</p></div>
    <div><div style="background:var(--purple);height:9px;color:#fff;font-size:4px;font-weight:700;line-height:9px">D</div><p class="tiny" style="margin-top:4px">Lorem ipsum dolor sit amet, consectetur adipiscing elit. Aenean sed tempor lorem.</p></div>
  </div>
  <div class="footer-mark"></div><div class="footer-line"></div>
</section>

<!-- 21 Quote -->
<section class="slide" style="left:338px;top:879px;background:#e6e6e6">
  <div class="photo" style="left:0;top:0;width:247px;height:70px;background:linear-gradient(180deg,#5b3fa0,#4b2d8f)" role="img" aria-label="Foliage under a purple overlay"></div>
  <div class="abs" style="left:10px;top:5px;font-size:12px;font-weight:700;color:#fff;line-height:12px">&ldquo;</div>
  <div class="abs" style="right:10px;top:52px;font-size:12px;font-weight:700;color:#fff;line-height:12px">&rdquo;</div>
  <p class="abs" style="left:30px;top:19px;width:187px;text-align:center;font-size:4.8px;line-height:6.4px;font-weight:600;color:#fff">&ldquo;Lorem ipsum dolor sit amet, consectetur adipiscing elit. Phasellus sodales, ligula ultrices tempus ristique, tellus justo aliquam dui, nec Lorem ipsum dolor sit amet, consectetur adipiscing elit. Lorem ipsum dolor sit amet, consectetur adipiscing&rdquo;</p>
  <div class="photo ph-portrait" style="left:105px;top:56px;width:37px;height:37px;border:2px solid #fff" role="img" aria-label="Speaker portrait"></div>
  <div class="abs" style="left:0;right:0;top:98px;text-align:center;font-size:5px;font-weight:600;color:#444">Renata Vale</div>
  <div class="abs" style="left:0;right:0;top:106px;text-align:center;font-size:3.2px;color:#888">Chief Operating Officer</div>
</section>

<!-- 22 Closing -->
<section class="slide" style="left:617px;top:879px">
  <div class="photo" style="inset:0;background:linear-gradient(120deg,#c9dd7a,#6f9a3a 45%,#4a3a25 80%,#6a8a3a)" role="img" aria-label="Meadow flowers beside a tree trunk"></div>
  <div class="abs" style="left:27px;top:0;width:93px;height:139px;background:rgba(75,45,143,.85)"></div>
  <div class="abs" style="left:27px;top:61px;width:93px;text-align:center;font-size:11px;font-weight:400;color:#fff">THANK YOU</div>
</section>

</body>
</html>
```